Granger Earthworks LLC business card design

Excavation company business cards

Contact Information for Business Card

Granger Earthworks LLC cell phone 208-555-0147 office phone 208-555-0193 grangerearthworksllc@mailnest.example Driveways, site prep, retaining walls, septic systems, rock delivery

Colors

Designer to choose colors to be used in the design.

```html
<!DOCTYPE html>
<html lang="en">
<head>
<meta charset="utf-8">
<title>Granger Earthworks LLC – Business Cards</title>
<link rel="stylesheet" href="https://fonts.googleapis.com/css2?family=Archivo:wght@400;600;800&display=swap">
<style>
  :root{
    --bg:#e6e6e8;
    --card-light:#ffffff;
    --card-dark:#2b2b2d;
    --orange:#f07a1e;
    --ink:#3d3d3f;
    --rule:#7a7a7c;
    --mark-dark:#4b4b4e;
    --service:#f2f2f2;
  }
  *{box-sizing:border-box;margin:0;padding:0}
  html,body{width:1200px;height:802px;overflow:hidden}
  body{background:var(--bg);font-family:"Archivo",Arial,sans-serif;position:relative}
  .card{position:absolute;top:252px;width:520px;height:298px;border-radius:3px;box-shadow:0 4px 14px rgba(0,0,0,.12)}
  .card--front{left:50px;background:var(--card-light)}
  .card--back{left:630px;background:var(--card-dark)}

  .brand{position:absolute;display:flex;align-items:center;gap:10px;font-weight:800;letter-spacing:.5px;text-transform:uppercase}
  .brand__dot{width:14px;height:14px;border-radius:50%;flex:none}
  .card--front .brand{top:52px;right:48px;color:var(--orange);font-size:24px}
  .card--front .brand__dot{background:var(--orange)}

  .person{position:absolute;left:40px;top:150px}
  .person__name{color:var(--orange);font-weight:800;font-size:19px;letter-spacing:.3px;text-transform:uppercase}
  .person__title{color:var(--ink);font-size:14px;margin-top:3px}
  .divider{position:absolute;left:40px;right:40px;top:206px;height:1px;background:var(--rule)}
  .contacts{position:absolute;left:40px;right:40px;top:222px;display:flex;flex-wrap:wrap;gap:8px 18px;font-size:13.5px;color:var(--ink)}
  .contact{display:flex;align-items:center;gap:6px}
  .contact svg{width:13px;height:13px;flex:none}

  .card--back .brand{top:96px;left:0;right:0;justify-content:center;color:var(--mark-dark);font-size:30px}
  .card--back .brand__dot{background:var(--mark-dark)}
  .services{position:absolute;left:0;right:0;top:178px;text-align:center;color:var(--service);font-size:15.5px;letter-spacing:.3px;text-transform:uppercase;line-height:1.75}
  .services span{white-space:nowrap}
  .services span::before{content:"";display:inline-block;width:8px;height:8px;border-radius:50%;background:var(--orange);margin:0 7px 2px 10px;vertical-align:middle}
</style>
</head>
<body>
  <section class="card card--front">
    <div class="brand"><span class="brand__dot"></span>Granger Earthworks LLC</div>
    <div class="person">
      <p class="person__name">Daniel Reyes</p>
      <p class="person__title">Manager</p>
    </div>
    <div class="divider"></div>
    <div class="contacts">
      <p class="contact">
        <svg viewBox="0 0 14 14" aria-hidden="true"><rect x="3" y="1" width="8" height="12" rx="1.5" fill="none" stroke="#f07a1e" stroke-width="1.5"/><line x1="6" y1="11" x2="8" y2="11" stroke="#f07a1e" stroke-width="1.2"/></svg>
        208-555-0147
      </p>
      <p class="contact">
        <svg viewBox="0 0 14 14" aria-hidden="true"><path d="M3 1.5l2.2 2.6-1.2 1.5c.9 1.8 2.4 3.3 4.4 4.4l1.5-1.2 2.6 2.2-1.3 1.7C6.4 12.4 1.6 7.6 1.3 2.8z" fill="#f07a1e"/></svg>
        208-555-0193
      </p>
      <p class="contact">
        <svg viewBox="0 0 14 14" aria-hidden="true"><rect x="1" y="3" width="12" height="8.5" fill="#f07a1e"/><path d="M1.5 3.5L7 8l5.5-4.5" fill="none" stroke="#fff" stroke-width="1.2"/></svg>
        grangerearthworksllc@mailnest.example
      </p>
    </div>
  </section>

  <section class="card card--back">
    <div class="brand"><span class="brand__dot"></span>Granger Earthworks LLC</div>
    <p class="services">
      <span>Driveways</span><span>Site Prep</span><br>
      <span>Retaining Walls</span><span>Septic Systems</span><span>Rock Delivery</span>
    </p>
  </section>
</body>
</html>
```